Tavio's Pizzeria Direct Mail Postcard

Looking for a direct mail postcard with a similar design as the one attached, with our logo and store information. This has to meet rlmt direct mail standards and have the postage block printed on the back of cards. I will send over text edits once we get the design we like. The back of the card can have store info and coupons, just have to make sure the coupons on the back dont match the same space as coupons on the front so customers can cut them out. Please use the attached card as a guide. I want to have the same basic design

Industry/Entity Type

Pizza Delivery

Colors

Designer to choose colors to be used in the design.

Requirements
Must have
• RLMT Direct Mail capability
Nice to have
• Great pictures

```html
<!DOCTYPE html>
<html lang="en">
<head>
<meta charset="utf-8">
<title>Tavio's Pizzeria – Direct Mail Postcard</title>
<link href="https://fonts.googleapis.com/css2?family=Baloo+2:wght@700;800&family=Open+Sans:wght@400;700&display=swap" rel="stylesheet">
<style>
  :root{
    --canvas:#c3b5a3;
    --paper:#ffffff;
    --brown:#4a3a31;
    --brown-dark:#3a2c24;
    --taupe:#b8ab9c;
    --red:#c8161d;
    --red-dark:#9e1016;
    --wall-light:#e4e2df;
    --wall:#9d948b;
    --badge:#d6cbbf;
    --badge-edge:#ffffff;
    --ink:#4a3a31;
    --line:#5b4a40;
  }
  *{box-sizing:border-box;margin:0;padding:0}
  html,body{width:1200px;height:696px;overflow:hidden}
  body{background:var(--canvas);position:relative;font-family:"Open Sans",sans-serif;color:var(--ink)}

  .postcard{position:absolute;width:555px;height:360px;overflow:hidden;background:var(--paper);box-shadow:0 4px 12px rgba(0,0,0,.28)}
  .postcard--back{left:30px;top:70px}
  .postcard--front{left:615px;top:70px}

  .photo{position:absolute}

  /* back */
  .back__photo{left:0;top:0;width:290px;height:150px;background:radial-gradient(ellipse 85% 90% at 42% 70%,#d06a3c 0%,#b8462c 40%,#6e3424 72%,#2e211b 100%)}
  .back__band{position:absolute;left:0;top:150px;width:290px;height:14px;background:var(--brown)}
  .back__wall{left:0;top:164px;width:290px;height:196px;background:linear-gradient(180deg,#d2cfcb 0%,var(--wall-light) 55%,#f1f0ee 100%)}
  .back__coupons{position:absolute;left:8px;top:176px;display:flex;gap:4px}
  .postage{position:absolute;right:30px;top:24px;width:100px;height:70px;border:2px solid var(--line)}
  .address-block{position:absolute;left:330px;top:180px;width:195px;display:flex;flex-direction:column;gap:31px}
  .address{border-top:1.5px solid var(--line)}

  /* coupons */
  .coupon{width:68px;height:68px;border-radius:50%;background:radial-gradient(circle,#e2d9cf 55%,var(--badge));border:4px dotted var(--badge-edge);box-shadow:0 0 0 2px var(--badge),0 2px 4px rgba(0,0,0,.2);display:flex;flex-direction:column;align-items:center;justify-content:center;line-height:1;text-align:center;color:var(--ink)}
  .coupon__amount{font-family:"Baloo 2",sans-serif;font-weight:800;font-size:20px;display:flex;align-items:flex-start;line-height:.9}
  .coupon__stack{display:flex;flex-direction:column;align-items:flex-start;margin-left:1px}
  .coupon__cents{font-size:9px;line-height:1}
  .coupon__any{font-size:9px;line-height:1}
  .coupon__off{font-weight:700;font-size:9px;margin-top:1px}
  .coupon__size{font-size:6px;margin-top:1px}
  .coupon__item{font-weight:700;font-size:6px}
  .coupon--large{width:112px;height:112px;border-width:6px}
  .coupon--large .coupon__amount{font-size:34px}
  .coupon--large .coupon__cents,.coupon--large .coupon__any{font-size:15px}
  .coupon--large .coupon__off{font-size:15px;margin-top:2px}
  .coupon--large .coupon__size{font-size:11px;margin-top:2px}
  .coupon--large .coupon__item{font-size:11px}

  /* front */
  .front__wall{left:0;top:0;width:555px;height:360px;background:linear-gradient(135deg,#8a7f75 0%,#a79e95 35%,#b6aea5 60%,#8f857b 100%)}
  .front__produce{left:300px;top:0;width:255px;height:70px;background:linear-gradient(90deg,#b9361f 0%,#d5452b 30%,#6f9a3a 55%,#a63a25 80%,#b3261a 100%)}
  .front__pie{left:400px;top:55px;width:210px;height:210px;border-radius:50%;background:radial-gradient(circle,#e7853f 0%,#d0522d 55%,#b07a45 70%,#7b5a3b 100%)}
  .front__slice{left:0;top:145px;width:262px;height:185px;background:radial-gradient(ellipse at 40% 50%,#eec060 0%,#d36a31 45%,#a3321f 75%,#6e2618 100%)}

  .headline{position:absolute;left:52px;top:14px;font-family:"Baloo 2",sans-serif;font-weight:800;font-size:46px;line-height:.95;color:#fff;text-shadow:2px 2px 0 var(--brown),-2px -2px 0 var(--brown),2px -2px 0 var(--brown),-2px 2px 0 var(--brown),3px 4px 4px rgba(0,0,0,.4)}
  .headline__line{display:block}
  .headline__dollar{font-size:28px}

  .front__base{position:absolute;left:0;top:0;width:555px;height:360px}
  .front__coupon-left{position:absolute;left:128px;top:226px}
  .front__coupon-right{position:absolute;left:330px;top:236px}

  .brand{position:absolute;display:flex;align-items:center;gap:7px;font-family:"Baloo 2",sans-serif;font-weight:800;color:var(--red);white-space:nowrap;line-height:1}
  .brand__dot{width:12px;height:12px;border-radius:50%;background:var(--red);flex:none}
  .front__brand{left:270px;top:188px;transform:translateX(-50%);font-size:22px;background:#fff;padding:6px 12px;border-radius:20px;box-shadow:0 2px 5px rgba(0,0,0,.25)}
  .standalone-brand{left:60px;top:565px;font-size:40px}
  .standalone-brand .brand__dot{width:22px;height:22px}
</style>
</head>
<body>

  <section class="postcard postcard--back" aria-label="Postcard back">
    <div class="photo back__photo" role="img" aria-label="Close-up photo of a vegetable pizza with olives, peppers and mushrooms"></div>
    <div class="back__band"></div>
    <div class="photo back__wall" role="img" aria-label="Faded light stone wall texture"></div>
    <div class="back__coupons">
      <div class="coupon"><span class="coupon__amount">$3<span class="coupon__stack"><span class="coupon__cents">00</span><span class="coupon__any">any</span></span></span><span class="coupon__off">off</span><span class="coupon__size">12" or 14"</span><span class="coupon__item">Pizza</span></div>
      <div class="coupon"><span class="coupon__amount">$3<span class="coupon__stack"><span class="coupon__cents">00</span><span class="coupon__any">any</span></span></span><span class="coupon__off">off</span><span class="coupon__size">12" or 14"</span><span class="coupon__item">Pizza</span></div>
      <div class="coupon"><span class="coupon__amount">$3<span class="coupon__stack"><span class="coupon__cents">00</span><span class="coupon__any">any</span></span></span><span class="coupon__off">off</span><span class="coupon__size">12" or 14"</span><span class="coupon__item">Pizza</span></div>
      <div class="coupon"><span class="coupon__amount">$3<span class="coupon__stack"><span class="coupon__cents">00</span><span class="coupon__any">any</span></span></span><span class="coupon__off">off</span><span class="coupon__size">12" or 14"</span><span class="coupon__item">Pizza</span></div>
    </div>
    <div class="postage"></div>
    <div class="address-block">
      <div class="address"></div>
      <div class="address"></div>
      <div class="address"></div>
      <div class="address"></div>
    </div>
  </section>

  <section class="postcard postcard--front" aria-label="Postcard front">
    <div class="photo front__wall" role="img" aria-label="Grey stone brick wall background"></div>
    <div class="photo front__produce" role="img" aria-label="Fresh tomatoes, lettuce, peppercorns and sausages"></div>
    <div class="photo front__pie" role="img" aria-label="Whole pizza with salami, tomatoes and olives on a wooden board"></div>
    <div class="photo front__slice" role="img" aria-label="Supreme pizza with a slice being lifted, cheese stretching"></div>

    <h1 class="headline"><span class="headline__line">14" Party</span><span class="headline__line">Pizza <span class="headline__dollar">$</span>10.00</span></h1>

    <svg class="front__base" viewBox="0 0 555 360" aria-hidden="true">
      <polygon points="0,252 120,252 120,290 0,290 10,271" fill="var(--red)"/>
      <polygon points="435,252 555,252 545,271 555,290 435,290" fill="var(--red)"/>
      <polygon points="140,215 420,215 555,330 555,360 0,360 0,330" fill="var(--brown)"/>
      <polygon points="140,215 150,215 20,330 0,330" fill="var(--taupe)"/>
      <polygon points="410,215 420,215 555,330 535,330" fill="var(--taupe)"/>
      <rect x="0" y="330" width="555" height="30" fill="var(--brown-dark)"/>
    </svg>

    <div class="brand front__brand"><span class="brand__dot"></span>Tavio's Pizzeria</div>

    <div class="coupon coupon--large front__coupon-left"><span class="coupon__amount">$3<span class="coupon__stack"><span class="coupon__cents">00</span><span class="coupon__any">any</span></span></span><span class="coupon__off">off</span><span class="coupon__size">12" or 14"</span><span class="coupon__item">Pizza</span></div>
    <div class="coupon coupon--large front__coupon-right"><span class="coupon__amount">$3<span class="coupon__stack"><span class="coupon__cents">00</span><span class="coupon__any">any</span></span></span><span class="coupon__off">off</span><span class="coupon__size">12" or 14"</span><span class="coupon__item">Pizza</span></div>
  </section>

  <div class="brand standalone-brand"><span class="brand__dot"></span>Tavio's Pizzeria</div>

</body>
</html>
```